Looking for a professional, clean and crisp business card

I am in the underground utilities industry and am just looking for a really impressive business card. I would like our card to be white with our symbol crisp and clear with it protruding. I also have a business partner that will require his name and info on the card once the design is set. I would like to have our website info on the card which is;
http://granitetrenchco.example/

Contact Information for Business Card

Website, contact name, number and email

```html
<!DOCTYPE html>
<html lang="en">
<head>
<meta charset="utf-8">
<title>Granite Trench Co — Business Card</title>
<link href="https://fonts.googleapis.com/css2?family=Montserrat:wght@400;700;800&display=swap" rel="stylesheet">
<style>
  :root {
    --backdrop: #d9d7d5;
    --card: #ffffff;
    --card-pattern: #f2f2f2;
    --ink: #1c1c1c;
    --brand-blue: #3a5fa8;
    --bar: #1a1a1a;
    --bar-text: #ffffff;
  }
  * { box-sizing: border-box; margin: 0; padding: 0; }
  html, body {
    width: 1200px; height: 884px; overflow: hidden;
    background: var(--backdrop);
    font-family: "Montserrat", sans-serif;
    color: var(--ink);
  }
  .canvas { position: relative; width: 1200px; height: 884px; }

  .card {
    position: absolute;
    background: var(--card);
    box-shadow: 0 8px 24px rgba(0,0,0,0.12);
  }

  /* Front: vertical contact side */
  .card-front {
    left: 110px; top: 122px; width: 380px; height: 640px;
    display: flex; flex-direction: column; align-items: center;
    padding-top: 54px;
  }
  .brand-mark {
    display: flex; flex-direction: column; align-items: center; gap: 12px;
  }
  .brand-dot {
    width: 22px; height: 22px; border-radius: 50%;
    background: var(--brand-blue);
  }
  .brand-name {
    font-weight: 800; font-size: 24px; letter-spacing: 0.04em;
    text-transform: uppercase; color: var(--ink); text-align: center;
  }
  .contacts { margin-top: 46px; display: flex; flex-direction: column; gap: 34px; text-align: center; }
  .contact-name {
    color: var(--brand-blue); font-weight: 700; font-size: 21px;
    text-transform: uppercase; letter-spacing: 0.02em;
  }
  .contact-role { font-size: 15px; margin-top: 4px; }
  .contact-rule { width: 26px; height: 2px; background: var(--ink); margin: 10px auto; }
  .contact-line { font-size: 15px; line-height: 1.5; }

  .web-bar {
    position: absolute; left: 28px; right: 28px; bottom: 30px; height: 40px;
    background: var(--bar); color: var(--bar-text);
    display: flex; align-items: center; justify-content: center;
    font-size: 15px; letter-spacing: 0.02em;
  }
  .web-bar::before, .web-bar::after {
    content: ""; position: absolute; top: -7px; width: 9px; height: 54px;
    background: var(--bar);
  }
  .web-bar::before { left: -12px; }
  .web-bar::after { right: -12px; }

  /* Back: horizontal brand side */
  .card-back {
    left: 560px; top: 262px; width: 560px; height: 360px;
    background: var(--card-pattern);
    display: flex; flex-direction: column; align-items: center; justify-content: center;
  }
  .card-back .brand-name { font-size: 32px; }
  .card-back .brand-dot { width: 28px; height: 28px; }
  .back-web { margin-top: 52px; font-size: 19px; letter-spacing: 0.02em; }
</style>
</head>
<body>
<main class="canvas">
  <section class="card card-front">
    <div class="brand-mark">
      <span class="brand-dot"></span>
      <span class="brand-name">Granite Trench Co</span>
    </div>
    <div class="contacts">
      <div class="contact">
        <p class="contact-name">Dale Whitcombe</p>
        <p class="contact-role">Owner</p>
        <div class="contact-rule"></div>
        <p class="contact-line">604-555-0142(DIGS)</p>
        <p class="contact-line">Dale@granitetrenchco.example</p>
      </div>
      <div class="contact">
        <p class="contact-name">Reid Halvorsen</p>
        <p class="contact-role">Owner</p>
        <div class="contact-rule"></div>
        <p class="contact-line">604-555-0187(DIGS)</p>
        <p class="contact-line">Reid@granitetrenchco.example</p>
      </div>
    </div>
    <div class="web-bar">www.granitetrenchco.example</div>
  </section>

  <section class="card card-back" role="img" aria-label="Light grey repeating maple leaf pattern behind the company name">
    <div class="brand-mark">
      <span class="brand-dot"></span>
      <span class="brand-name">Granite Trench Co</span>
    </div>
    <p class="back-web">www.granitetrenchco.example</p>
  </section>
</main>
</body>
</html>
```